Modern and Improved business card design for Family Dental Practice

We have 2 sets of logo we have designed and now just need a business card layout and design for the office. Colors are on the logo. We can choose which logo we want to go with . The font can be changed to whatever seems modern and relevant. We are family dental office that has been open for over 15 years in South Austin Texas.

Target Market(s)

Handout Business cards to referrals and specialists

Industry/Entity Type

Dental

Contact Information for Business Card

We need address, phone, website and email address. 4830 North Maple Loop Suite 208 , Austin,Texas 78392....phone: 512-847-3195.....email- info@bluepinedental.example....website - BluePineDental.example

Font styles to use
Serif
Decorative

Requirements
Must have
• my logo. We have 2 logos, but we can use just one or if we can incorporate one on one side and the other on the other side.
Nice to have
• Really just need a modern look and clean that incorporates the logo and colors .

```html
<!DOCTYPE html>
<html lang="en">
<head>
<meta charset="utf-8">
<title>Blue Pine Family Dentistry – Business Card</title>
<link rel="stylesheet" href="https://fonts.googleapis.com/css2?family=Questrial&family=Arimo:wght@400;700&display=swap">
<style>
  :root {
    --page: #e9e9e6;
    --card-dark: #1c1c1c;
    --card-light: #f6f6f6;
    --brand-green: #0b7a0f;
    --ink-dark: #1f1f1f;
    --ink-light: #ffffff;
  }
  * { box-sizing: border-box; margin: 0; padding: 0; }
  html, body { width: 1200px; height: 768px; overflow: hidden; }
  body {
    background: var(--page);
    display: flex;
    align-items: center;
    justify-content: center;
    gap: 40px;
    font-family: "Arimo", Arial, sans-serif;
  }
  .card {
    position: relative;
    width: 560px;
    height: 320px;
    overflow: hidden;
    box-shadow: 0 6px 18px rgba(0,0,0,0.18);
  }
  .card--front { background: var(--card-dark); border-bottom: 3px solid var(--brand-green); }
  .card--back { background: var(--card-light); }

  .brand {
    display: flex;
    align-items: center;
    gap: 14px;
    font-family: "Questrial", "Century Gothic", sans-serif;
  }
  .brand__dot { border-radius: 50%; background: var(--brand-green); flex: none; }
  .brand__name { line-height: 1.1; text-transform: uppercase; letter-spacing: 1px; white-space: nowrap; }

  .card--front .brand {
    position: absolute; left: 50%; top: 50%;
    transform: translate(-50%, -50%);
  }
  .card--front .brand__dot { width: 60px; height: 60px; }
  .card--front .brand__name { color: var(--ink-light); font-size: 30px; }

  .card--back .brand { position: absolute; left: 40px; top: 36px; gap: 12px; }
  .card--back .brand__dot { width: 38px; height: 38px; }
  .card--back .brand__name { color: var(--ink-dark); font-size: 18px; }

  .band { position: absolute; inset: 0; width: 100%; height: 100%; }

  .contact {
    position: absolute;
    right: 28px;
    top: 150px;
    text-align: right;
    color: var(--ink-light);
    font-size: 13.5px;
    line-height: 1.35;
  }
  .contact__name { font-size: 21px; font-weight: 700; line-height: 1.1; }
  .contact__title { font-size: 14px; margin-bottom: 6px; }
  .contact__line { display: flex; justify-content: flex-end; align-items: center; gap: 8px; white-space: nowrap; }
  .contact__icon { width: 13px; height: 13px; flex: none; }
  .contact__spacer { display: inline-block; width: 13px; }
  .contact__gap { height: 6px; }
</style>
</head>
<body>

  <section class="card card--front" aria-label="Card front">
    <div class="brand">
      <span class="brand__dot"></span>
      <span class="brand__name">Blue Pine<br>Family Dentistry</span>
    </div>
  </section>

  <section class="card card--back" aria-label="Card back">
    <svg class="band" viewBox="0 0 560 320" preserveAspectRatio="none" aria-hidden="true">
      <path d="M410,0 C330,40 258,170 224,320 L560,320 L560,0 Z" fill="var(--brand-green)"/>
      <path d="M396,0 C316,40 244,170 210,320" fill="none" stroke="var(--brand-green)" stroke-width="3"/>
    </svg>

    <div class="brand">
      <span class="brand__dot"></span>
      <span class="brand__name">Blue Pine<br>Family Dentistry</span>
    </div>

    <div class="contact">
      <p class="contact__name">Daniel Mercer</p>
      <p class="contact__title">Managing Director</p>
      <p class="contact__line">4830 North Maple Loop<span class="contact__spacer"></span></p>
      <p class="contact__line">Suite 208, Austin, Texas 78392<span class="contact__spacer"></span></p>
      <div class="contact__gap"></div>
      <p class="contact__line">512-847-3195
        <svg class="contact__icon" viewBox="0 0 16 16" aria-hidden="true"><path fill="#fff" d="M3.6 1.2l2.3 2.6-1.3 1.8c.9 2 2.5 3.6 4.5 4.6l1.8-1.3 2.6 2.3-1.3 2.3C6.9 13.4 2.6 9.1 1.4 2.5z"/></svg>
      </p>
      <p class="contact__line">info@bluepinedental.example
        <svg class="contact__icon" viewBox="0 0 16 16" aria-hidden="true"><rect x="1" y="3" width="14" height="10" fill="#fff"/><path d="M1.5 3.5L8 9l6.5-5.5" fill="none" stroke="var(--brand-green)" stroke-width="1.4"/></svg>
      </p>
      <p class="contact__line">www.BluePineDental.example
        <svg class="contact__icon" viewBox="0 0 16 16" aria-hidden="true"><circle cx="8" cy="8" r="7" fill="#fff"/><path d="M1 8h14M8 1c-3 3.5-3 10.5 0 14M8 1c3 3.5 3 10.5 0 14" fill="none" stroke="var(--brand-green)" stroke-width="1.1"/></svg>
      </p>
    </div>
  </section>

</body>
</html>
```